Musician looking for catchy Web Design for promotion

My name is Bridget Colfer. I'm an Irish musician who plays the tin whistle and the flute. I'm also the leader of a traditional Irish music and dance ensemble called Rowan Road Players (www.rowanroadplayers.test) and for the past 30 years, I've toured the world performing thousands of concerts. I run an annual cruise (www.bridgetcolfercruise.test) that I would like a link to, and I'm also I'm organizing tours to Ireland that I would like a page set up for. I'm looking for a website to promote my tours and my music.

Hello Graphic Designers, I am only looking for the design of the home page to make my decision. Thank you. Bridget

Target Market(s)

Music fans of Irlsh and World Music

Industry/Entity Type

Entertainment Industry

Number of Pages Required

5+ page

Requirements
Must have
• I'm looking for a catchy design that shows a photo of me. I would like a few links....
• BIO
• TOURDATES
• BRIDGET COLFER CRUISE
• MUSICAL TOUR OF IRELAND
• CONTACT
• VIDEO
• GALLERY
• CONTACT
• MAILING LIST
• STORE
Nice to have
• we'll see!

```html
<!DOCTYPE html>
<html lang="en">
<head>
<meta charset="utf-8">
<title>Bridget Colfer – Home</title>
<link href="https://fonts.googleapis.com/css2?family=Great+Vibes&family=Libre+Baskerville:wght@400;700&family=Open+Sans:wght@400;600;700&display=swap" rel="stylesheet">
<style>
  :root {
    --gold: #b9974a;
    --gold-dark: #9c7c35;
    --ink: #1a1a1a;
    --text: #333333;
    --muted: #777777;
    --accent-red: #c0392b;
    --white: #ffffff;
    --footer-bg: #0b0b0b;
    --brown-deep: #2a1a10;
    --brown-mid: #6b4a2c;
    --brass: #c9a86a;
  }
  * { box-sizing: border-box; margin: 0; padding: 0; }
  html, body { width: 1200px; height: 3750px; overflow: hidden; background: var(--white); }
  body { font-family: "Open Sans", Arial, sans-serif; color: var(--text); position: relative; }

  /* Header */
  .site-header { position: absolute; top: 0; left: 0; width: 1200px; height: 110px; display: flex; align-items: center; justify-content: space-between; padding: 0 40px 0 50px; background: var(--white); }
  .brand { display: flex; align-items: center; gap: 12px; font-family: "Open Sans", Arial, sans-serif; font-weight: 700; font-size: 20px; letter-spacing: 1px; color: var(--ink); white-space: nowrap; }
  .brand-dot { width: 34px; height: 34px; border-radius: 50%; background: var(--ink); flex: none; }
  .main-nav { display: flex; gap: 22px; font-size: 15px; font-weight: 600; white-space: nowrap; }
  .main-nav a { color: var(--ink); text-decoration: none; }
  .main-nav a.is-active { color: var(--accent-red); }

  /* Hero */
  .hero { position: absolute; top: 110px; left: 0; width: 1200px; height: 940px; background: radial-gradient(ellipse at 50% 45%, var(--brass) 0%, var(--brown-mid) 45%, var(--brown-deep) 100%); overflow: hidden; }
  .hero-tile { position: absolute; width: 250px; height: 250px; transform: rotate(45deg); border: 6px solid var(--white); }
  .tile-a { left: 270px; top: 300px; background: linear-gradient(135deg, #4a3a30, #1d1612); }
  .tile-b { left: 495px; top: 130px; background: linear-gradient(135deg, #3a2a35, #120e12); }
  .tile-c { left: 680px; top: 245px; background: linear-gradient(135deg, #cfd9d2, #8fa58c); }
  .tile-d { left: 435px; top: 450px; background: linear-gradient(135deg, #4e3747, #1c1418); }
  .tile-e { left: 625px; top: 505px; background: linear-gradient(135deg, #8a6e86, #3b2a38); }
  .hero-name { position: absolute; left: 0; width: 100%; top: 820px; line-height: 100px; text-align: center; font-family: "Great Vibes", cursive; font-size: 78px; color: var(--white); }

  /* Welcome */
  .welcome { position: absolute; top: 1050px; left: 0; width: 1200px; height: 650px; }
  .welcome-portrait { position: absolute; left: 60px; top: 235px; width: 230px; height: 230px; border-radius: 50%; background: linear-gradient(160deg, #7a6a60, #2b2320); }
  .welcome-kicker { position: absolute; left: 330px; top: 120px; font-family: "Libre Baskerville", Georgia, serif; font-size: 68px; color: var(--gold); letter-spacing: 1px; }
  .welcome-title { position: absolute; left: 330px; top: 215px; font-family: "Libre Baskerville", Georgia, serif; font-size: 52px; font-weight: 400; color: var(--ink); }
  .welcome-text { position: absolute; left: 330px; top: 300px; width: 800px; font-family: "Libre Baskerville", Georgia, serif; font-size: 14.5px; line-height: 30px; color: var(--ink); }

  /* Video */
  .video { position: absolute; left: 240px; top: 1735px; width: 720px; height: 255px; background: linear-gradient(180deg, #9fc4e6 0%, #5f8fbd 45%, #2c5e91 100%); box-shadow: 0 6px 18px rgba(0,0,0,.35); }
  .video-play { position: absolute; left: 310px; top: 78px; width: 100px; height: 100px; }
  .video-bar { position: absolute; left: 0; bottom: 0; width: 100%; height: 44px; background: rgba(10,20,35,.55); }

  /* Travel */
  .travel-title { position: absolute; top: 2015px; width: 100%; text-align: center; font-family: "Libre Baskerville", Georgia, serif; font-size: 36px; font-weight: 700; color: var(--ink); }
  .travel-text { position: absolute; top: 2075px; left: 70px; width: 1060px; font-size: 14px; line-height: 25px; color: var(--text); }

  /* About band */
  .about { position: absolute; top: 2290px; left: 0; width: 1200px; height: 460px; background: linear-gradient(180deg, #3b2516 0%, #1f140c 60%, #2e1d11 100%); color: var(--white); }
  .about-title { position: absolute; top: 60px; width: 100%; text-align: center; font-family: "Libre Baskerville", Georgia, serif; font-size: 40px; }
  .about-kicker { position: absolute; top: 128px; width: 100%; text-align: center; font-family: "Libre Baskerville", Georgia, serif; font-size: 20px; letter-spacing: 2px; }
  .about-text { position: absolute; top: 185px; left: 120px; width: 980px; font-family: "Libre Baskerville", Georgia, serif; font-size: 21px; line-height: 34px; }

  /* Features */
  .features { position: absolute; top: 2810px; left: 40px; width: 1120px; display: flex; justify-content: space-between; }
  .feature { width: 260px; text-align: center; }
  .feature-icon { width: 180px; height: 180px; margin: 0 auto; border-radius: 50%; border: 2px solid #dddddd; display: flex; align-items: center; justify-content: center; }
  .feature-title { margin-top: 38px; font-size: 22px; font-weight: 600; color: var(--ink); letter-spacing: 1px; }
  .feature-text { margin-top: 10px; font-size: 14px; line-height: 20px; color: var(--muted); }
  .feature-btn { display: inline-block; margin-top: 16px; padding: 6px 18px; background: var(--gold); color: var(--white); font-size: 13px; font-weight: 600; }

  /* Footer */
  .site-footer { position: absolute; top: 3260px; left: 0; width: 1200px; height: 490px; background: var(--footer-bg); color: var(--white); padding: 85px 50px 0; display: flex; }
  .footer-col { width: 265px; }
  .footer-col h4 { font-size: 20px; font-weight: 700; letter-spacing: 1px; margin-bottom: 26px; }
  .footer-col li { list-style: none; font-size: 18px; line-height: 30px; }
  .social { display: flex; gap: 12px; }
  .social span { width: 46px; height: 46px; border-radius: 50%; background: var(--white); }
</style>
</head>
<body>

<header class="site-header">
  <div class="brand"><span class="brand-dot"></span>BRIDGET COLFER</div>
  <nav class="main-nav">
    <a class="is-active" href="#">Bio</a>
    <a href="#">Tourdates</a>
    <a href="#">Cruise</a>
    <a href="#">Musical Tour of Ireland</a>
    <a href="#">Video</a>
    <a href="#">Gallery</a>
    <a href="#">Mailing List</a>
    <a href="#">Store</a>
    <a href="#">Contact</a>
  </nav>
</header>

<section class="hero" role="img" aria-label="Close-up of wooden and silver flutes and tin whistles on a warm brown background">
  <div class="hero-tile tile-a" role="img" aria-label="Photo of Bridget playing flute on stage"></div>
  <div class="hero-tile tile-b" role="img" aria-label="Portrait photo of Bridget"></div>
  <div class="hero-tile tile-c" role="img" aria-label="Photo of a songbird"></div>
  <div class="hero-tile tile-d" role="img" aria-label="Photo of Bridget smiling"></div>
  <div class="hero-tile tile-e" role="img" aria-label="Photo of Bridget with her whistle"></div>
  <div class="hero-name">Bridget Colfer</div>
</section>

<section class="welcome">
  <div class="welcome-portrait" role="img" aria-label="Round portrait photo of Bridget"></div>
  <div class="welcome-kicker">HEY THERE!</div>
  <h1 class="welcome-title">WELCOME TO MY SITE</h1>
  <p class="welcome-text">BRIDGET COLFER is an award-winning whistle and flute player who has been the leader of Rowan Road Players since its inception. Born in New York to Irish parents, she is the second eldest of seven children raised in a musical household. Her mother, a dancer, and her father, a button accordion player, filled the home with tunes, sessions and visiting musicians. Bridget received her musical training early in life, listening to the fiddle and tin whistle at family gatherings and local events. She began taking lessons at the age of nine and within a few short years became the first American to win the senior whistle championship in Ireland.</p>
</section>

<div class="video" role="img" aria-label="Video still of a cruise ship sailing past a city skyline">
  <svg class="video-play" viewBox="0 0 100 100"><circle cx="50" cy="50" r="46" fill="rgba(255,255,255,.3)" stroke="#fff" stroke-width="4"/><polygon points="40,30 72,50 40,70" fill="#fff"/></svg>
  <div class="video-bar"></div>
</div>

<h2 class="travel-title">Travel Around My Soul</h2>
<p class="travel-text">It is simply impossible to imagine an audience that wouldn't enjoy what they hear. Join the Rowan Road Players on a journey across the sea, where every evening brings a new concert, a céilí on deck and a session that runs long past midnight. For more than three decades Bridget has toured the world, from grand concert halls to small village pubs, and now she invites you to travel with her. Each tour is planned around the music, with guest artists, dance workshops and plenty of time to explore the places where these tunes were born. Whether you play an instrument or simply love to listen, you will find friends, stories and songs waiting for you. Come along and let the music carry you home.</p>

<section class="about" role="img" aria-label="Dark brown background of flutes">
  <h2 class="about-title">Shortly About Bridget Colfer</h2>
  <div class="about-kicker">LET'S GET ACQUAINTED</div>
  <p class="about-text">Bridget has become one of the most visible Irish musicians in the world over the past two and a half decades. Not only is she renowned as a composer but also as a highly energetic and a totally entertaining stage performer. Her huge repertoire of music spans a wide range of expressions, from stunning dance tunes to slow, stately and evocative pieces. She is a consummate musician and one of the most successful and revered figures in Irish music today.</p>
</section>

<section class="features">
  <div class="feature">
    <div class="feature-icon"><svg width="80" height="80" viewBox="0 0 80 80"><circle cx="40" cy="40" r="34" fill="var(--gold)"/><circle cx="40" cy="40" r="8" fill="#fff"/></svg></div>
    <div class="feature-title">NEW RELEASES</div>
    <p class="feature-text">New tunes and recordings<br>from the studio.</p>
    <span class="feature-btn">Read More</span>
  </div>
  <div class="feature">
    <div class="feature-icon"><svg width="80" height="80" viewBox="0 0 80 80"><rect x="10" y="14" width="60" height="56" fill="var(--gold)"/><g fill="#fff"><rect x="18" y="28" width="10" height="8"/><rect x="35" y="28" width="10" height="8"/><rect x="52" y="28" width="10" height="8"/><rect x="18" y="44" width="10" height="8"/><rect x="35" y="44" width="10" height="8"/><rect x="52" y="44" width="10" height="8"/></g></svg></div>
    <div class="feature-title">TOUR SCHEDULE</div>
    <p class="feature-text">Concerts and sessions coming<br>to your town.</p>
    <span class="feature-btn">Read More</span>
  </div>
  <div class="feature">
    <div class="feature-icon"><svg width="80" height="80" viewBox="0 0 80 80"><circle cx="52" cy="26" r="16" fill="var(--gold)"/><line x1="42" y1="38" x2="16" y2="66" stroke="var(--gold)" stroke-width="8" stroke-linecap="round"/></svg></div>
    <div class="feature-title">LATEST PARTIES</div>
    <p class="feature-text">Photos and stories from<br>recent celebrations.</p>
    <span class="feature-btn">Read More</span>
  </div>
  <div class="feature">
    <div class="feature-icon"><svg width="80" height="80" viewBox="0 0 80 80"><g fill="var(--gold)"><rect x="12" y="40" width="8" height="30"/><rect x="26" y="22" width="8" height="48"/><rect x="40" y="10" width="8" height="60"/><rect x="54" y="30" width="8" height="40"/></g></svg></div>
    <div class="feature-title">MY HOT REMIX</div>
    <p class="feature-text">Fresh arrangements of<br>old favourite tunes.</p>
    <span class="feature-btn">Read More</span>
  </div>
</section>

<footer class="site-footer">
  <div class="footer-col">
    <h4>EVENT INFO</h4>
    <ul><li>Artists</li><li>Contact Us</li><li>Mailing List</li></ul>
  </div>
  <div class="footer-col">
    <h4>PRICES</h4>
    <ul><li>Prices Per Person</li><li>What's Included?</li><li>Payment Options</li><li>Travel Insurance</li><li>Book Now!</li></ul>
  </div>
  <div class="footer-col">
    <h4>FAQ</h4>
    <ul><li>Top Questions</li><li>Before You Book</li><li>Placing Reservations</li><li>Automatic Billing</li><li>Manage Reservations</li><li>Pre-Cruise Details</li><li>Once Onboard</li></ul>
  </div>
  <div class="footer-col">
    <h4>FOLLOW ME:</h4>
    <div class="social"><span></span><span></span><span></span><span></span></div>
  </div>
</footer>

</body>
</html>
```